Harbor Ridge Decks

Looking for a vehicle wrap for a 2019 Veltrano Brisko Haulmax. Also interested in t-shirt and Polo design similar to the type of stuff "Pinwheel Studios" designs.
If possible I would like the front and back of the vehicle wrap to transition into silver so I don't have to wrap my grill and bumpers (Veltrano frost moon metalic).
Vehicle wrap elements should include:
•HarborRidgeDecks.example
•Free Estimates
•LA 📞 555-014-DECK
•MS 📞 555-027-DECK
•Patio Covers
•Screen Rooms
•Sunrooms
•3 Season Rooms

```html
<!DOCTYPE html>
<html lang="en">
<head>
<meta charset="utf-8">
<title>Harbor Ridge Decks – Vehicle Wrap</title>
<link rel="stylesheet" href="https://fonts.googleapis.com/css2?family=Montserrat:wght@400;500&family=Nunito:wght@800;900&display=swap">
<style>
  :root {
    --silver: #d9dde0;
    --silver-light: #eef1f3;
    --sky: #5bbde6;
    --sky-deep: #2fa9e0;
    --purple: #8a4f9c;
    --purple-deep: #6e3a86;
    --ink: #1b1b1f;
    --white: #ffffff;
    --crab-blue: #3a86d0;
    --crab-purple: #6b3c9a;
  }
  * { box-sizing: border-box; margin: 0; padding: 0; }
  html, body { width: 1200px; height: 1200px; overflow: hidden; background: var(--white); }
  .canvas { position: relative; width: 1200px; height: 1200px; }

  /* Side panel */
  .side-wrap {
    position: absolute; left: 40px; top: 150px; width: 1120px; height: 330px;
    border-radius: 18px; overflow: hidden;
    background: linear-gradient(90deg, var(--silver) 0%, var(--silver-light) 22%, #bfe3f4 42%, var(--sky) 62%, var(--purple) 63%, var(--purple-deep) 100%);
  }
  .side-wrap .swoosh { position: absolute; left: 690px; top: 0; width: 120px; height: 330px; }
  .brand {
    position: absolute; display: flex; align-items: center; gap: 10px;
  }
  .brand-mark { width: 22px; height: 22px; border-radius: 50%; background: var(--sky-deep); }
  .brand-name {
    font-family: "Montserrat", sans-serif; font-weight: 500; letter-spacing: 2px;
    text-transform: uppercase; color: var(--purple);
  }
  .side-wrap .brand { left: 70px; top: 70px; }
  .side-wrap .brand-name { font-size: 24px; }
  .brand-rule { position: absolute; height: 2px; background: var(--sky-deep); }
  .side-wrap .brand-rule.top { left: 70px; top: 118px; width: 270px; }
  .side-wrap .brand-rule.bottom { left: 70px; top: 158px; width: 270px; }
  .tagline {
    position: absolute; font-family: "Montserrat", serif; font-size: 11px; letter-spacing: 9px;
    color: var(--purple); text-transform: uppercase;
  }
  .side-wrap .tagline { left: 110px; top: 130px; }

  .services {
    position: absolute; left: 60px; top: 215px;
    font-family: "Nunito", sans-serif; font-weight: 900; font-size: 19px; color: var(--ink);
    line-height: 1.3;
  }
  .services .sep { margin: 0 10px; font-weight: 400; }

  .url {
    position: absolute; font-family: "Montserrat", sans-serif; font-weight: 500;
    letter-spacing: 1px; text-transform: uppercase;
  }
  .side-wrap .url { left: 420px; top: 26px; font-size: 13px; color: var(--ink); }

  .mascot {
    position: absolute; border-radius: 50%;
    background: radial-gradient(circle at 50% 50%, var(--crab-blue) 0%, var(--crab-purple) 45%, rgba(255,255,255,0.35) 70%, rgba(255,255,255,0) 72%);
  }
  .side-wrap .mascot { left: 520px; top: 40px; width: 280px; height: 280px; }

  .contact { position: absolute; font-family: "Nunito", sans-serif; font-weight: 900; color: var(--white); }
  .side-wrap .contact { left: 835px; top: 30px; }
  .estimates { color: var(--sky); font-size: 26px; letter-spacing: 1px; text-align: center; }
  .phone-line { font-size: 27px; line-height: 1.25; display: flex; align-items: center; gap: 8px; }
  .phone-icon { width: 20px; height: 20px; flex: none; }

  /* Tailgate panel */
  .tailgate {
    position: absolute; left: 330px; top: 620px; width: 540px; height: 320px;
    border-radius: 14px; overflow: hidden; background: var(--sky-deep);
  }
  .tailgate .cab-band { position: absolute; left: 0; top: 0; width: 100%; height: 40px; background: var(--sky); }
  .tailgate .gate {
    position: absolute; left: 20px; top: 50px; width: 500px; height: 260px; border-radius: 6px;
    background: linear-gradient(120deg, var(--purple) 0%, #9a66ad 60%, var(--purple-deep) 100%);
  }
  .tailgate .brand { left: 30px; top: 40px; }
  .tailgate .brand-mark { width: 16px; height: 16px; }
  .tailgate .brand-name { font-size: 17px; color: var(--white); }
  .tailgate .brand-rule { background: var(--sky); }
  .tailgate .brand-rule.top { left: 30px; top: 72px; width: 210px; }
  .tailgate .brand-rule.bottom { left: 30px; top: 100px; width: 210px; }
  .tailgate .tagline { left: 70px; top: 80px; color: var(--sky); font-size: 9px; }
  .tailgate .url { left: 240px; top: 12px; font-size: 12px; color: var(--white); }
  .tailgate .contact { left: 20px; top: 160px; }
  .tailgate .phone-line { font-size: 24px; }
  .tailgate .mascot { left: 310px; top: 60px; width: 200px; height: 200px; }
</style>
</head>
<body>
<main class="canvas">

  <section class="side-wrap" aria-label="Side panel of the wrap">
    <svg class="swoosh" viewBox="0 0 120 330" aria-hidden="true">
      <path d="M80 0 C 60 110, 20 200, 0 330" fill="none" stroke="#5bbde6" stroke-width="10"/>
    </svg>

    <div class="brand"><span class="brand-mark"></span><span class="brand-name">Harbor Ridge Decks</span></div>
    <div class="brand-rule top"></div>
    <div class="tagline">Decks</div>
    <div class="brand-rule bottom"></div>

    <div class="services">
      <div>Patio Covers<span class="sep">|</span>Screen Rooms</div>
      <div>Sunrooms<span class="sep">|</span>3 Season Rooms</div>
    </div>

    <div class="url">HarborRidgeDecks.example</div>

    <div class="mascot" role="img" aria-label="Cartoon blue crab mascot holding a bottle, with light rays behind"></div>

    <div class="contact">
      <div class="estimates">Free Estimates</div>
      <div class="phone-line">LA 555-014-DECK</div>
      <div class="phone-line">MS 555-027-DECK</div>
    </div>
  </section>

  <section class="tailgate" aria-label="Rear tailgate of the wrap">
    <div class="cab-band"></div>
    <div class="gate">
      <div class="url">HarborRidgeDecks.example</div>
      <div class="brand"><span class="brand-mark"></span><span class="brand-name">Harbor Ridge Decks</span></div>
      <div class="brand-rule top"></div>
      <div class="tagline">Decks</div>
      <div class="brand-rule bottom"></div>

      <div class="mascot" role="img" aria-label="Cartoon blue crab mascot holding a bottle, with light rays behind"></div>

      <div class="contact">
        <div class="phone-line">LA
          <svg class="phone-icon" viewBox="0 0 24 24" aria-hidden="true"><path fill="#5bbde6" d="M6.6 10.8a15.1 15.1 0 0 0 6.6 6.6l2.2-2.2a1 1 0 0 1 1-.25 11.4 11.4 0 0 0 3.6.57 1 1 0 0 1 1 1V20a1 1 0 0 1-1 1A17 17 0 0 1 3 4a1 1 0 0 1 1-1h3.5a1 1 0 0 1 1 1c0 1.25.2 2.45.57 3.57a1 1 0 0 1-.25 1z"/></svg>
          555-014-DECK</div>
        <div class="phone-line">MS
          <svg class="phone-icon" viewBox="0 0 24 24" aria-hidden="true"><path fill="#5bbde6" d="M6.6 10.8a15.1 15.1 0 0 0 6.6 6.6l2.2-2.2a1 1 0 0 1 1-.25 11.4 11.4 0 0 0 3.6.57 1 1 0 0 1 1 1V20a1 1 0 0 1-1 1A17 17 0 0 1 3 4a1 1 0 0 1 1-1h3.5a1 1 0 0 1 1 1c0 1.25.2 2.45.57 3.57a1 1 0 0 1-.25 1z"/></svg>
          555-027-DECK</div>
      </div>
    </div>
  </section>

</main>
</body>
</html>
```